Bluegate Gatherings Web Design Layout (no HTML)

We require the layout only for a website.  No html or logo is required - just the layout.

A refreshed and revitalized website to coincide with the relaunch of our brand. We are looking for a clean simplistic design that is easy to use and presents relevant information effectively.
We are an events management company specializing in conferences.
Updates

Thank you for your design. We really like the imagery. Essentially we are after a home page design (one page) that incorporates the 3 main buttons (request a proposal, select a venue and specials) while providing the relevant information on our service via functionality similar to that on www.trelvasite.com ie using the large arrow to scroll over the relevant topic to receive information. We hope to finalise the contest in the next week and hope to consider your revised entry.

Thanks!

Target Market(s)

Australian corporate sector primarily Managing Directors or their assistants. Any business looking to hold a conference for up 500 delegates however we are primarily targeting the decision maker so need to ensure we are communicating on their terms.

Industry/Entity Type

Event

Requirements
Must have
• Incorporate the elements from the attached document however with complete creative license as to their layout. Our main competitors are pordamhosting.com.au, brimwellsummits.com.au both sites are bland and not user friendly.
Nice to have
• Colours red, silver and black. Note we are running a separate contest to refresh our logo.
• We like the functionality of trelvasite.com

```html
<!DOCTYPE html>
<html lang="en">
<head>
<meta charset="utf-8">
<title>Bluegate Gatherings – Complete Conference Solutions</title>
<link rel="stylesheet" href="https://fonts.googleapis.com/css2?family=Open+Sans:wght@400;600;700&family=Arimo:wght@400;700&display=swap">
<style>
:root{
  --red:#d8261f;
  --red-deep:#a11b17;
  --red-panel:#c8231d;
  --silver:#a9a9a9;
  --silver-light:#d4d4d4;
  --grey-page:#999999;
  --ink:#1a1a1a;
  --muted:#555555;
  --white:#ffffff;
}
*{margin:0;padding:0;box-sizing:border-box}
html,body{width:1200px;height:1059px;overflow:hidden}
body{background:var(--grey-page);font-family:"Open Sans",Arial,sans-serif;color:var(--ink);position:relative}
.page{position:absolute;left:39px;top:0;width:1122px;height:1059px;background:var(--white)}
.abs{position:absolute}
.top-band{left:70px;top:0;width:1066px;height:29px;background:linear-gradient(180deg,var(--red) 0%,var(--red-deep) 100%)}
.brand{left:131px;top:64px;display:flex;flex-direction:column}
.brand-row{display:flex;align-items:center;gap:12px}
.brand-mark{width:44px;height:44px;background:var(--red)}
.brand-name{font-family:"Arimo",Arial,sans-serif;font-weight:700;font-size:34px;color:var(--red);letter-spacing:-0.5px;line-height:1}
.brand-tag{font-family:"Arimo",Arial,sans-serif;font-size:13px;color:var(--muted);margin-left:56px;margin-top:2px}
.contact{left:777px;top:81px;font-size:15px;line-height:18px;color:var(--muted)}
.contact b{font-weight:700}
.nav{left:130px;top:136px;width:923px;height:36px;background:linear-gradient(180deg,#e6e6e6,#b5b5b5);border:1px solid #9a9a9a}
.nav-pointer{left:222px;top:171px}
.nav a{position:absolute;top:4px;width:114px;height:28px;border-radius:9px;background:linear-gradient(180deg,#ee3a30,var(--red-deep));border:1px solid #fff;color:var(--white);font-family:"Arimo",Arial,sans-serif;font-weight:700;font-size:15px;text-align:center;line-height:26px;text-decoration:none}
.feature h2{position:absolute;font-family:"Arimo",Arial,sans-serif;font-weight:400;font-size:28px;color:var(--red);white-space:nowrap}
.feature p{position:absolute;font-size:16.4px;line-height:20px;color:var(--ink)}
.art{position:absolute}
.panel-left{left:137px;top:366px;width:347px;height:574px;background:linear-gradient(135deg,var(--red) 0%,var(--red-deep) 100%)}
.panel-left .intro{position:absolute;left:32px;top:26px;width:290px;font-size:16.4px;line-height:22.3px;color:var(--white)}
.panel-left .intro b{font-weight:700}
.goal-band{left:137px;top:583px;width:347px;height:107px;background:linear-gradient(180deg,#bdbdbd,var(--silver))}
.goal-band .title{position:absolute;right:22px;top:30px;font-weight:600;font-size:26px;color:var(--white)}
.goal-band .rule{position:absolute;left:22px;top:66px;width:304px;height:3px;background:var(--white)}
.goal-arrow{left:476px;top:614px}
.goals{left:137px;top:705px;width:347px;list-style:none}
.goals li{position:absolute;left:98px;color:var(--white);font-weight:700;font-size:21px;line-height:30px;white-space:nowrap}
.goals li::before{content:"";position:absolute;left:-38px;top:8px;width:18px;height:18px;border-radius:50%;background:#e6e6e6}
.panel-right{left:516px;top:365px;width:542px;height:366px;background:linear-gradient(135deg,var(--red-panel) 0%,var(--red-deep) 100%)}
.panel-right .body{position:absolute;left:35px;top:30px;width:490px;font-size:16.4px;line-height:22.3px;color:var(--white)}
.panel-right ul{list-style:none}
.panel-right ul li::before{content:"• "}
.panel-right .summary{margin-top:22px}
.btn-learn{left:859px;top:658px;width:174px;height:49px;background:linear-gradient(180deg,#c9c9c9,#8f8f8f);border:1px solid #eee;color:var(--white);font-weight:600;font-size:27px;text-align:center;line-height:45px;text-decoration:underline}
.promo-flight{left:549px;top:751px;width:245px;height:98px;background:linear-gradient(90deg,#f4f4f4 0%,#d9e4ee 60%,#9fb7cc 100%);border-bottom:18px solid var(--red)}
.promo-currency{left:802px;top:751px;width:217px;height:28px;background:linear-gradient(180deg,#3f74c4,#1c4a96);color:var(--white);font-family:"Arimo",Arial,sans-serif;font-size:15px;line-height:28px;padding-left:34px}
.promo-currency .go,.promo-win .go{position:absolute;right:4px;bottom:3px;background:#d8d8d8;color:#333;font-size:11px;font-weight:700;padding:0 6px;line-height:15px}
.promo-currency .ico{position:absolute;left:6px;top:5px;width:20px;height:18px;background:#cfe0f5;border-radius:3px}
.promo-win{left:802px;top:793px;width:220px;height:57px;background:linear-gradient(180deg,#e8302a,#a5150f);color:var(--white);font-family:"Arimo",Arial,sans-serif;font-size:14.5px;line-height:17px;padding:8px 12px}
.promo-win b{font-size:18px}
.closing{left:520px;top:863px;width:560px;font-size:16.4px;line-height:22.3px;color:var(--ink)}
.closing a{color:var(--red);font-weight:700;font-size:19.5px;text-decoration:underline;margin-left:10px}
.footer{left:70px;top:995px;width:1066px;height:64px;background:linear-gradient(180deg,var(--red) 0%,var(--red-deep) 100%)}
.footer p{position:absolute;right:22px;top:20px;color:var(--white);font-size:16.4px}
.footer b{font-weight:700}
</style>
</head>
<body>
<div class="page"></div>
<div class="abs top-band"></div>

<header>
  <div class="abs brand">
    <div class="brand-row"><span class="brand-mark"></span><span class="brand-name">Bluegate Gatherings</span></div>
    <span class="brand-tag">Complete Conference Solutions</span>
  </div>
  <div class="abs contact">Ph: <b>1300 555 274</b>.<br>P.O. Box 4417, Harbourview NSW 2099.</div>
</header>

<nav class="abs nav">
  <a href="#" style="left:9px">home</a>
  <a href="#" style="left:140px">services</a>
  <a href="#" style="left:271px">venues</a>
  <a href="#" style="left:403px">clients</a>
  <a href="#" style="left:534px">register</a>
  <a href="#" style="left:668px">finance option</a>
  <a href="#" style="left:798px">contact us</a>
</nav>
<svg class="abs nav-pointer" width="20" height="18" viewBox="0 0 20 18"><polygon points="0,0 20,0 2,18" fill="#b5b5b5"/></svg>

<section class="feature">
  <h2 style="left:135px;top:205px">Browse Conference</h2>
  <div class="art" role="img" aria-label="Red map of Australia with state labels" style="left:135px;top:244px;width:111px;height:108px;background:radial-gradient(circle at 50% 45%,#e8302a,#b51a14 70%,transparent 72%)"></div>
  <p style="left:256px;top:246px;width:200px">Not sure where to start? We have over 60 properties to choose from both domestically and international.</p>

  <h2 style="left:468px;top:205px">Request a Proposal</h2>
  <div class="art" role="img" aria-label="Red wall clock illustration" style="left:468px;top:244px;width:88px;height:90px;border-radius:50%;background:radial-gradient(circle,#ffffff 55%,#d8261f 58%,#9c1712 100%)"></div>
  <p style="left:568px;top:246px;width:160px">Prefer us to do the leg work?We can prepare andreturn a proposal within 24 hours of receipt.</p>

  <h2 style="left:771px;top:205px">Special Offer</h2>
  <div class="art" role="img" aria-label="Red dollar sign illustration" style="left:768px;top:249px;width:74px;height:98px;background:linear-gradient(135deg,#f07a72,#c8231d 60%,#8c1410)"></div>
  <p style="left:852px;top:246px;width:230px">Always looking for a bargain? Save money with one of our special offers available for a limited time.</p>
</section>

<section class="abs panel-left">
  <p class="intro"><b>Bluegate Gatherings’</b> professional conference team specialises in solutions. We work closely with a core group of clients to ensure desired outcomes, on time and in budget.<br><br>Our goal is to make sure your conference is;</p>
</section>
<div class="abs goal-band"><span class="title">Cost Effective</span><span class="rule"></span></div>
<svg class="abs goal-arrow" width="42" height="52" viewBox="0 0 42 52"><polygon points="0,0 42,0 0,52" fill="#a9a9a9"/><polygon points="0,0 8,0 8,42 0,52" fill="#c8231d"/></svg>
<ul class="abs goals">
  <li style="top:0">Expertly Managed<br>and Hassle Free</li>
  <li style="top:88px">Outcome focused</li>
  <li style="top:150px">Well Attended</li>
</ul>

<section class="abs panel-right">
  <div class="body">
    <p>We offer a complete range of finance&nbsp; packages including;</p>
    <ul>
      <li>total conference underwriting</li>
      <li>online delegate payment gateway</li>
      <li>substantially discounted rooming rates</li>
      <li>no upfront costs</li>
      <li>zero management fees</li>
      <li>free venue sourcing</li>
      <li>free delegate booking management</li>
    </ul>
    <p class="summary">Minimise your costs and free your cash flow to focus on your core business functions. We’ll ensure maximum return from your conference budget.</p>
  </div>
</section>
<a class="abs btn-learn" href="#">Learn how?</a>

<div class="abs promo-flight" role="img" aria-label="Domestic flight sale banner with aircraft photo, fares from 28 dollars one way"></div>
<div class="abs promo-currency"><span class="ico"></span>Convert Currency<span class="go">go »</span></div>
<div class="abs promo-win"><b>WIN</b> tickets to L.A.<br>Bali or Marla Vey in concert<span class="go">go »</span></div>

<p class="abs closing">Bluegate Gatherings’ professional conference team specialises in solutions. We work closely with a core group of clients to ensure desired outcomes, on time and in budget.<a href="#">Learn how?</a></p>

<footer class="abs footer"><p>Copyright <b>Bluegate Gatherings</b>. All Rights Reserved. 2009</p></footer>
</body>
</html>
```